National Sales Meeting Agenda (Rodeo Theme)

I need a talented designer to create a visually stunning, single-page agenda for our upcoming National Sales Meeting. The design should reflect our brand’s colors and style, with a subtle rodeo theme, while maintaining a professional and polished look.
Key Requirements:
Theme: Subtle rodeo vibe with clean, Western-inspired elements that align with our brand identity.
Branding: Prominently feature the KORA FLEX TM logo, with a smaller LUMAR logo included.
Layout: Single page, clean, sharp, and easy to read.
Content: Include the meeting date (June 6-7) and location (Copper Ridge Lodge Scottsdale) at the top.
Formats: High-quality, print-ready PDF + editable file (Canva or InDesign) for updates.
Timeline: First draft within 1-2 days, final version by May 23rd.
Deliverables:
Print-ready PDF
Editable file for future updates
Design that captures our brand tone and subtle rodeo theme
Please visit koraflextm.example for brand inspiration. Let me know if you have any questions or need additional assets. Looking forward to seeing your creative ideas!
Target Market(s)
Medical Device Sales Reps
Look and feel

```html
<!DOCTYPE html>
<html lang="en">
<head>
<meta charset="utf-8">
<title>National Sales Meeting Agenda</title>
<link href="https://fonts.googleapis.com/css2?family=Barlow+Condensed:wght@400;500;600;700&family=Barlow+Semi+Condensed:wght@400;500;600;700&display=swap" rel="stylesheet">
<style>
:root{
  --navy:#1c2547;
  --ink:#2a2f3f;
  --muted:#5a5f6e;
  --grey-star:#a6a9b1;
  --rule:#1c2547;
  --dots:#9a9ea8;
  --paper:#f5f5f7;
  --display:"Barlow Condensed",sans-serif;
  --text:"Barlow Semi Condensed",sans-serif;
}
*{margin:0;padding:0;box-sizing:border-box}
html,body{width:848px;height:1200px;overflow:hidden;background:var(--paper)}
body{position:relative;font-family:var(--text);color:var(--ink)}
.abs{position:absolute}
.icon-star{width:18px;height:18px;fill:var(--navy);display:block}
.kicker{left:88px;top:64px;font-family:var(--display);font-weight:500;font-size:20px;color:var(--navy);letter-spacing:.5px}
.title{left:48px;top:92px;display:flex;align-items:center;gap:12px}
.title .icon-star{width:26px;height:26px}
.title h1{font-family:var(--display);font-weight:500;font-size:48px;color:var(--navy);line-height:1;letter-spacing:.2px}
.venue{left:88px;top:146px;font-family:var(--text);font-size:15px;color:var(--muted);letter-spacing:.3px}
.brand{right:62px;top:94px;font-family:var(--display);font-weight:700;font-size:42px;color:var(--navy);line-height:1;letter-spacing:.5px}
.day{left:66px;display:flex;align-items:center;gap:6px;font-family:var(--display);font-weight:400;font-size:21px;color:var(--muted)}
.day .icon-star{fill:var(--grey-star);width:20px;height:20px}
.table-head{left:86px;width:696px;display:flex;font-family:var(--display);font-weight:600;font-size:20px;color:var(--navy)}
.table-head .col-time{width:81px}
.table-head .col-topic{flex:1}
.rule{left:67px;width:714px;height:1.5px;background:var(--rule)}
.row{left:86px;width:712px;display:flex;align-items:center;font-size:16px}
.row .time{width:81px;flex:none}
.row .topic{width:220px;flex:none}
.row .leader{flex:1;border-bottom:1.5px dotted var(--dots);height:1px;margin:0 10px 0 14px;transform:translateY(3px)}
.row .presenter{text-align:right;line-height:1.1}
.row .presenter.two{font-size:15px;line-height:1.05}
.row .mark{width:40px;flex:none;display:flex;flex-direction:column;align-items:flex-end;gap:3px}
.row.break .topic{font-family:var(--display);font-weight:700;color:var(--navy);font-size:16px;letter-spacing:.4px;width:auto}
.split{left:167px;display:flex;gap:60px;font-size:15px}
.split .group-title{display:flex;align-items:center;gap:4px}
.split .icon-star{width:15px;height:15px}
.split ul{list-style:none;margin-left:22px;font-size:13px;line-height:17px;margin-top:2px}
.split ul li::before{content:"• "}
.mascot{left:356px;top:1070px;width:136px;height:112px;border-radius:50%;background:radial-gradient(ellipse at center,rgba(28,37,71,.55) 0%,rgba(28,37,71,.25) 50%,rgba(28,37,71,0) 72%)}
.partner{right:66px;top:1108px;font-family:var(--display);font-weight:600;font-size:40px;color:var(--navy);letter-spacing:1px;line-height:1}
</style>
</head>
<body>
<svg width="0" height="0" style="position:absolute" aria-hidden="true">
  <defs>
    <symbol id="star" viewBox="0 0 24 24"><path d="M12 1.5l3.1 7.1 7.7.6-5.9 5 1.8 7.5L12 17.7l-6.7 4 1.8-7.5-5.9-5 7.7-.6z"/></symbol>
  </defs>
</svg>

<header>
  <div class="abs kicker">AGENDA</div>
  <div class="abs title"><svg class="icon-star"><use href="#star"/></svg><h1>National Sales Meeting</h1></div>
  <div class="abs venue">June 6–7, 2025 &nbsp;·&nbsp; Copper Ridge Lodge Scottsdale</div>
  <div class="abs brand">KORA FLEX TM</div>
</header>

<div class="abs day" style="top:174px"><svg class="icon-star"><use href="#star"/></svg>Friday, June 6, 2025</div>
<div class="abs table-head" style="top:224px"><span class="col-time">TIME</span><span class="col-topic">TOPIC DESCRIPTION</span><span class="col-presenter">PRESENTER</span></div>
<div class="abs rule" style="top:251px"></div>

<div class="abs row break" style="top:268px"><span class="time">7:30 am</span><span class="topic">BREAKFAST</span></div>
<div class="abs row" style="top:299px"><span class="time">8:30 am</span><span class="topic">Welcome &amp; Meeting Overview</span><span class="leader"></span><span class="presenter">Dean Harlow</span><span class="mark"><svg class="icon-star"><use href="#star"/></svg></span></div>
<div class="abs row" style="top:332px"><span class="time">9:00 am</span><span class="topic">MRI Review Exercise</span><span class="leader" style="border:0"></span><span class="presenter">Wes Porter</span><span class="mark"><svg class="icon-star"><use href="#star"/></svg></span></div>
<div class="abs row break" style="top:364px"><span class="time">9:45 am</span><span class="topic">BREAK</span></div>
<div class="abs row" style="top:396px"><span class="time">10:00 am</span><span class="topic">Objection Handling</span><span class="leader"></span><span class="presenter">Cole Brandt</span><span class="mark"><svg class="icon-star"><use href="#star"/></svg></span></div>
<div class="abs row" style="top:429px"><span class="time">11:00 am</span><span class="topic">CEV Expectations</span><span class="leader"></span><span class="presenter">Dean Harlow</span><span class="mark"><svg class="icon-star"><use href="#star"/></svg></span></div>
<div class="abs row break" style="top:459px"><span class="time">11:30 am</span><span class="topic">LUNCH</span></div>
<div class="abs row" style="top:492px"><span class="time">12:00 pm</span><span class="topic">Afternoon Split Session</span><span class="leader"></span><span class="presenter">ALL</span><span class="mark"><svg class="icon-star"><use href="#star"/></svg></span></div>
<div class="abs split" style="top:522px">
  <div class="group">
    <div class="group-title"><svg class="icon-star"><use href="#star"/></svg>Area Sales Managers</div>
    <ul><li>Leadership<br>&nbsp;&nbsp;Training</li><li>Field Operations</li></ul>
  </div>
  <div class="group">
    <div class="group-title"><svg class="icon-star"><use href="#star"/></svg>Associate Sales Representatives</div>
    <ul><li>APP Training</li><li>Coding &amp; Reimbursement</li></ul>
  </div>
</div>
<div class="abs row" style="top:604px"><span class="time">1:00 pm</span><span class="topic">Role Plays</span><span class="leader"></span><span class="presenter two">Grant Ellery<br>&amp; Miles Avery</span><span class="mark"><svg class="icon-star"><use href="#star"/></svg></span></div>
<div class="abs row" style="top:646px"><span class="time">1:30 pm</span><span class="topic">Day One Closing</span><span class="leader"></span><span class="presenter">Tomas Reyes</span><span class="mark"><svg class="icon-star"><use href="#star"/></svg></span></div>
<div class="abs row break" style="top:684px"><span class="time">2:00 pm</span><span class="topic">ADJOURN - RIVER RODEO</span></div>

<div class="abs day" style="top:737px"><svg class="icon-star"><use href="#star"/></svg>Saturday, June 7, 2025</div>
<div class="abs table-head" style="top:788px"><span class="col-time">TIME</span><span class="col-topic">TOPIC DESCRIPTION</span><span class="col-presenter">PRESENTER</span></div>
<div class="abs rule" style="top:817px"></div>

<div class="abs row break" style="top:832px"><span class="time">7:30 am</span><span class="topic">BREAKFAST</span></div>
<div class="abs row" style="top:864px"><span class="time">8:30 am</span><span class="topic" style="width:auto">RENEW &amp; ELEVATE Clinical Study Discussion</span><span class="leader"></span><span class="presenter">Jenna Whitlock</span><span class="mark"><svg class="icon-star"><use href="#star"/></svg></span></div>
<div class="abs row" style="top:899px"><span class="time">9:00 am</span><span class="topic" style="width:auto">TM Pilot 6 month, 12month, and 24 month Data</span><span class="leader"></span><span class="presenter">Tess Calloway</span><span class="mark"><svg class="icon-star"><use href="#star"/></svg></span></div>
<div class="abs row break" style="top:931px"><span class="time">10:00 am</span><span class="topic">BREAK</span></div>
<div class="abs row" style="top:962px"><span class="time">10:15 am</span><span class="topic">Veterans Administration</span><span class="leader"></span><span class="presenter two">Paige Lindqvist<br>&amp; Brent Hollis</span><span class="mark"><svg class="icon-star" style="width:15px;height:15px"><use href="#star"/></svg><svg class="icon-star" style="width:15px;height:15px"><use href="#star"/></svg></span></div>
<div class="abs row" style="top:1005px"><span class="time">11:00 am</span><span class="topic">Marketing Update</span><span class="leader"></span><span class="presenter">Avery Stroud</span><span class="mark"><svg class="icon-star"><use href="#star"/></svg></span></div>
<div class="abs row" style="top:1036px"><span class="time">11:30 am</span><span class="topic">2025 NSM Meeting Close</span><span class="leader"></span><span class="presenter">Dean Harlow</span><span class="mark"><svg class="icon-star"><use href="#star"/></svg></span></div>
<div class="abs row break" style="top:1067px"><span class="time">11:45 am</span><span class="topic">ADJOURN</span></div>

<div class="abs mascot" role="img" aria-label="Silhouette of a rodeo rider on a galloping horse swinging a lasso"></div>
<div class="abs partner">LUMAR</div>
</body>
</html>
```